Screening Mammography flyer for patients

We need a flyer design to inform our patients of our Screening Mammography program (it's a screening Diagnostic Imaging test). Women aged 50-74 years old are eligible for this exam. We also have a convenient booking system, when a patient can call us directly. There's no doctor’s referral needed to sign up for the test.
We are also starting the TLR Scanwell Envoy program, when select patients will help spread the word and save lives.
The flyer has to be done with a lot of pink color as it is a traditional color for Breast cancer materials, with consideration of the hospital's corporate colors (the brand book is attached).

Diagnostic Imaging

```html
<!DOCTYPE html>
<html lang="en">
<head>
<meta charset="utf-8">
<title>Just Book It! Screening Mammography Program</title>
<link rel="stylesheet" href="https://fonts.googleapis.com/css2?family=Open+Sans:wdth,wght@75..100,400..800&family=Oswald:wght@500;700&display=swap">
<style>
  :root {
    --pink: #e8679a;
    --pink-deep: #d94c86;
    --magenta: #e0237a;
    --purple: #6a3d9a;
    --teal: #0f7b87;
    --teal-ring: #1ea7b5;
    --green: #7ab73e;
    --lime: #b5d334;
    --white-panel: #f3f3f5;
    --ink: #4a4a4a;
    --white: #ffffff;
  }
  * { margin: 0; padding: 0; box-sizing: border-box; }
  html, body { width: 986px; height: 1200px; overflow: hidden; background: var(--pink); }
  .flyer { position: relative; width: 986px; height: 1200px; overflow: hidden; font-family: "Open Sans", sans-serif; }
  .backdrop { position: absolute; inset: 0; }
  .abs { position: absolute; }

  .headline {
    left: 210px; top: 58px;
    font-family: "Oswald", sans-serif; font-weight: 700;
    font-size: 104px; line-height: 1; letter-spacing: -3px;
    color: var(--purple); white-space: nowrap;
  }
  .program-name {
    left: 209px; top: 166px;
    font-family: "Oswald", sans-serif; font-weight: 700;
    font-size: 31px; line-height: 1; letter-spacing: 1.9px;
    color: var(--green); white-space: nowrap;
  }
  .hospital-name {
    left: 147px; top: 240px; width: 397px; height: 94px;
    display: flex; align-items: center; gap: 24px;
  }
  .hospital-name .mark { width: 70px; height: 70px; background: var(--green); flex: none; }
  .hospital-name span {
    font-weight: 700; font-size: 27px; line-height: 1.12; color: var(--ink); letter-spacing: 1px;
  }
  .network-rule { left: 147px; top: 346px; width: 397px; height: 2px; background: var(--green); }
  .network-name {
    left: 147px; top: 356px; width: 397px; text-align: center;
    font-weight: 700; font-size: 20px; line-height: 1.2; letter-spacing: 2.4px;
    color: var(--green); white-space: nowrap;
  }
  .audience {
    left: 150px; top: 423px; width: 392px; text-align: right;
    font-weight: 800; font-stretch: 75%; font-size: 64px; line-height: 57px;
    color: var(--teal); white-space: nowrap;
  }
  .badge {
    left: 357px; top: 557px; width: 184px; height: 184px; border-radius: 50%;
    background: var(--white); border: 7px solid var(--magenta);
    display: flex; flex-direction: column; align-items: flex-end; justify-content: center;
    padding-right: 20px; font-family: "Oswald", sans-serif; font-weight: 700;
    color: var(--magenta); line-height: 0.95; text-align: right;
  }
  .badge .lg { font-size: 32px; }
  .badge .sm { font-size: 15px; letter-spacing: 0.5px; }
  .photo {
    left: 568px; top: 210px; width: 366px; height: 634px;
    border-radius: 150px 150px 40px 40px;
    background: linear-gradient(180deg, #f0c6d3 0%, #f4a8c4 40%, #4d6b99 70%, #3c5684 100%);
    opacity: 0.9;
  }
  .benefits { left: 48px; top: 688px; width: 400px; list-style: none; }
  .benefits li {
    position: relative; padding-left: 34px; color: var(--white);
    font-weight: 600; font-size: 24px; line-height: 36px; white-space: nowrap;
    text-shadow: 0 1px 3px rgba(0,0,0,0.25); margin-bottom: 14px;
  }
  .benefits li::before {
    content: ""; position: absolute; left: 0; top: 10px; width: 16px; height: 16px;
    border-radius: 50%; background: var(--lime); border: 2px solid #5a7d1a;
  }
  .appointment-card {
    left: 53px; top: 870px; width: 463px; height: 97px; background: #e7e7ea;
    box-shadow: 0 3px 6px rgba(0,0,0,0.25); padding: 10px 12px;
  }
  .appointment-card h3 { font-weight: 700; font-size: 22px; color: var(--green); }
  .appointment-card p { margin-top: 22px; font-size: 15px; color: var(--ink); display: flex; }
  .appointment-card p::after { content: ""; flex: 1; border-bottom: 1px dotted var(--ink); margin: 0 12px 4px 3px; }
  .envoy-tab {
    left: 107px; top: 967px; width: 342px; height: 177px; background: var(--lime);
    border-radius: 0 0 26px 26px; box-shadow: 4px 5px 0 var(--pink-deep);
    text-align: center; color: var(--white); text-shadow: 0 1px 3px rgba(0,0,0,0.25);
    padding-top: 12px;
  }
  .envoy-tab h3 { font-weight: 600; font-size: 27px; line-height: 36px; margin-bottom: 8px; }
  .envoy-tab p { font-weight: 600; font-size: 24px; line-height: 32px; }
  .booking {
    left: 540px; width: 390px; text-align: center; color: var(--white);
    font-family: "Oswald", sans-serif; text-shadow: 0 2px 3px rgba(0,0,0,0.3); white-space: nowrap;
  }
  .booking-label { top: 865px; font-weight: 500; font-size: 38px; line-height: 42px; letter-spacing: -0.8px; }
  .booking-phone { top: 920px; font-weight: 700; font-size: 50px; line-height: 50px; }
  .booking-ext { top: 975px; font-weight: 700; font-size: 34px; line-height: 36px; }
  .contact-rule { left: 542px; top: 1037px; width: 388px; height: 4px; background: var(--lime); }
  .contact {
    left: 536px; width: 400px; text-align: center; color: var(--white);
    text-shadow: 0 1px 2px rgba(0,0,0,0.3); white-space: nowrap;
  }
  .contact-line { font-weight: 600; font-size: 15px; line-height: 20px; }
  .contact-one { top: 1064px; }
  .contact-two { top: 1093px; }
  .contact-web { top: 1118px; font-weight: 700; font-size: 23px; line-height: 30px; }
</style>
</head>
<body>
<div class="flyer">
  <svg class="backdrop" width="986" height="1200" viewBox="0 0 986 1200" aria-hidden="true">
    <rect width="986" height="1200" fill="var(--pink)"/>
    <rect x="700" y="0" width="286" height="320" fill="var(--pink-deep)" opacity="0.6"/>
    <circle cx="430" cy="265" r="470" fill="var(--green)"/>
    <circle cx="440" cy="252" r="460" fill="var(--purple)"/>
    <circle cx="520" cy="262" r="412" fill="var(--teal-ring)"/>
    <circle cx="520" cy="262" r="400" fill="var(--white-panel)"/>
  </svg>

  <h1 class="abs headline">JUST BOOK IT!</h1>
  <p class="abs program-name">SCREENING MAMMOGRAPHY PROGRAM</p>

  <div class="abs hospital-name">
    <div class="mark"></div>
    <span>HARLOW CREST<br>HOSPITAL</span>
  </div>
  <div class="abs network-rule"></div>
  <p class="abs network-name">EASTVALE HEALTH NETWORK</p>

  <h2 class="abs audience">FOR WOMEN<br>AGED 50-74</h2>

  <div class="abs photo" role="img" aria-label="Photo of three women of different ages in pink tops and jeans, embracing and smiling"></div>

  <div class="abs badge">
    <span class="lg">EARLY</span>
    <span class="sm">DETECTION</span>
    <span class="lg">SAVES</span>
    <span class="lg">LIVES</span>
  </div>

  <ul class="abs benefits">
    <li>No doctor’s referral<br>needed for your<br>Screening Mammogram</li>
    <li>Same Day appointments available !</li>
  </ul>

  <div class="abs appointment-card">
    <h3>Your Appointment’s</h3>
    <p>Date &amp; Time:</p>
  </div>

  <div class="abs envoy-tab">
    <h3>Envoy Program</h3>
    <p>Join the TLR Scanwell<br>Envoy Program to<br>help save lives!</p>
  </div>

  <p class="abs booking booking-label">TO BOOK AN APPOINTMENT</p>
  <p class="abs booking booking-phone">555-014-2290</p>
  <p class="abs booking booking-ext">ext 4410</p>

  <div class="abs contact-rule"></div>
  <p class="abs contact contact-line contact-one">Diagnostic Imaging @ Harlow Crest Hospital:</p>
  <p class="abs contact contact-line contact-two">410 Brightmoor Ave. Email: imaging@evhn.example</p>
  <p class="abs contact contact-web">www.evhn.example/imaging</p>
</div>
</body>
</html>
```